Mobile Recording Studio needs business cards

Open to seeing a creative design, but I want to emphasis my logo and minimize the name/title and company information. Possible a fully black background on card.

My company is a mobile sound recording studio. ok to include a my trailer (actual or cartoon) on the card. My initial thought is more straight forward, but a good design will win me over.

SPECS:
CMYK color mode
High (300ppi) raster effect.
cover bleed area
please deliver: Illustrator file with layers and a pdf at completion.

Name and info for the business card:

Dallin Perry
ADR Mixer

email: Dallin@MixVault.com

address:
248 - 5170 East Hollister
Vancouver, BC V5R 2J4

phone:
604.518.2093 office

website:
www.MixVault.com

FB: @MixVault

Instagram: @TheMixVault

Industry/Entity Type

Television Production

Contact Information for Business Card

Dallin Perry
ADR Mixer

email: Dallin@MixVault.com

address:
248 - 5170 East Hollister
Vancouver, BC V5R 2J4

phone:
604.518.2093 office

website:
www.MixVault.com

FB: @MixVault

Instagram: @TheMixVault

Colors

Designer to choose colors to be used in the design.

Requirements
Must have
• emphasis my logo and minimize the name/title and company information.
• SPECS:
• CMYK color mode
• High (300ppi) raster effect.
• cover bleed area
• please deliver: Illustrator file with layers and a pdf at completion.
Nice to have
• maybe include the following:
• all black background or black theme
• my work trailer (actual or cartoon) refer to Instagram: @TheMixVault

```html
<!DOCTYPE html>
<html lang="en">
<head>
<meta charset="utf-8">
<title>MixVault Business Card</title>
<link href="https://fonts.googleapis.com/css2?family=Lato:wght@400;700&family=Raleway:wght@700&display=swap" rel="stylesheet">
<style>
  :root {
    --page-bg: #e6e3df;
    --card-top: #606060;
    --card-bottom: #4c4c4c;
    --ink: #ffffff;
    --ink-soft: #ececec;
    --metal: #d6d6d6;
    --metal-dark: #8a8a8a;
  }
  html, body {
    margin: 0;
    padding: 0;
    width: 1200px;
    height: 900px;
    overflow: hidden;
    background: var(--page-bg);
  }
  .canvas {
    position: relative;
    width: 1200px;
    height: 900px;
  }
  .card {
    position: absolute;
    width: 556px;
    height: 343px;
    background: linear-gradient(180deg, var(--card-top), var(--card-bottom));
    color: var(--ink);
    font-family: "Lato", Arial, sans-serif;
  }
  .card--front { left: 330px; top: 90px; }
  .card--back { left: 331px; top: 470px; height: 342px; }

  .brand {
    position: absolute;
    font-family: "Lato", Arial, sans-serif;
    font-weight: 700;
    color: var(--metal);
    letter-spacing: 1px;
    line-height: 1;
  }
  .card--front .brand { right: 50px; top: 78px; font-size: 44px; }
  .card--back .brand { left: 0; right: 0; top: 144px; text-align: center; font-size: 60px; }

  .person { position: absolute; left: 28px; }
  .person__name {
    font-family: "Raleway", Arial, sans-serif;
    font-weight: 700;
    font-size: 18px;
    letter-spacing: 0.3px;
    margin: 0;
    text-transform: uppercase;
  }
  .person__title { font-size: 14.5px; margin: 3px 0 0 1px; color: var(--ink-soft); }
  .person--first { top: 170px; }
  .person--second { top: 227px; }

  .contact {
    position: absolute;
    right: 40px;
    top: 200px;
    text-align: right;
  }
  .contact__phone { font-size: 19px; margin: 0 0 12px; letter-spacing: 0.3px; }
  .contact__address { font-size: 15px; margin: 0; line-height: 19px; color: var(--ink-soft); }

  .divider {
    position: absolute;
    left: 28px;
    right: 38px;
    top: 285px;
    height: 3px;
    background: linear-gradient(90deg, var(--metal-dark), #f2f2f2 50%, var(--metal-dark));
  }

  .links {
    position: absolute;
    left: 28px;
    right: 38px;
    top: 299px;
    display: flex;
    justify-content: space-between;
    font-size: 15.5px;
  }
  .links__item { display: flex; align-items: center; gap: 5px; }
  .links__icon { width: 19px; height: 19px; flex: none; }
</style>
</head>
<body>
<main class="canvas">
  <section class="card card--front" aria-label="Card front">
    <div class="brand">MixVault</div>

    <div class="person person--first">
      <h2 class="person__name">Dallin Perry</h2>
      <p class="person__title">ADR Mixer</p>
    </div>
    <div class="person person--second">
      <h2 class="person__name">Reid Calloway</h2>
      <p class="person__title">Engineer / Director of Operations</p>
    </div>

    <div class="contact">
      <p class="contact__phone">604.518.2093</p>
      <p class="contact__address">248 - 5170 East Hollister</p>
      <p class="contact__address">Vancouver, BC V5R 2J4</p>
    </div>

    <div class="divider"></div>

    <div class="links">
      <span class="links__item">
        <svg class="links__icon" viewBox="0 0 20 20" aria-hidden="true">
          <circle cx="10" cy="10" r="9" fill="#fff"/>
          <circle cx="10" cy="10" r="6" fill="none" stroke="#555" stroke-width="1.2"/>
          <ellipse cx="10" cy="10" rx="2.6" ry="6" fill="none" stroke="#555" stroke-width="1.2"/>
          <line x1="4" y1="10" x2="16" y2="10" stroke="#555" stroke-width="1.2"/>
        </svg>
        www.MixVault.com
      </span>
      <span class="links__item">
        <svg class="links__icon" viewBox="0 0 20 20" aria-hidden="true"><circle cx="10" cy="10" r="9" fill="#fff"/></svg>
        @MixVault
      </span>
      <span class="links__item">
        <svg class="links__icon" viewBox="0 0 20 20" aria-hidden="true"><rect x="1.5" y="1.5" width="17" height="17" rx="3" fill="#fff"/></svg>
        @TheMixVault
      </span>
    </div>
  </section>

  <section class="card card--back" aria-label="Card back">
    <div class="brand">MixVault</div>
  </section>
</main>
</body>
</html>
```